"Every Lantern Still Burning" Sermon Series Design

Needing a design for our church's next sermon series titled "Every Lantern Still Burning" where we will discuss the need for unity, diversity, love and clarity. Looking for a 1920 x 1080 (or higher res) editable and layered file (PSD or AI) so that we can reformat the design to work on social, screens, lower thirds and various print and online mediums. We will also need to have access to the font files so that we can make resize and tweak as needed. We like the idea of using a globe or map of the world as the backdrop with the words overtop. Or, the idea of creating a bunch of newspaper clippings (generic, so that they can't actually be read) and making the shape of a heart. See attached examples. This website will give you an idea of our previous sermon series designs so you can have an idea of our style (but, feel free to help us advance the ball on something more aligned with current design trends): https://www.brinmoorfellowship.church/series

Examples use red, but stay away from a ton of red. If you're gonna major in a color, use blue or something in that family.

Must haves:
Title: Every Lantern Still Burning
Tagline : (TBD - use some Lorem Ipsum as a placeholder and we will fill in later)
Our Logo (attached) (small towards bottom is standard - only use solid colors for logo - preferably just solid black or white)

Industry/Entity Type

Church

Font styles to use
Serif
Sans Serif

Requirements
Must have
• Title: Every Lantern Still Burning
Nice to have
• We like the idea of using a globe or map of the world as the backdrop with the words overtop. Or, the idea of creating a bunch of newspaper clippings (generic, so that they can't actually be read) and making the shape of a heart. See attached examples.

If you're gonna major on a color, stick with blue or something close.
Should not have
• Don't use red as the primary color (example we sent has red, but stay away from it)

```html
<!DOCTYPE html>
<html lang="en">
<head>
<meta charset="utf-8">
<title>Every Lantern Still Burning — Sermon Series</title>
<link rel="stylesheet" href="https://fonts.googleapis.com/css2?family=Cinzel:wght@400;500;600&display=swap">
<style>
  :root {
    --sky: #2b99e3;
    --sky-light: #6bb8ea;
    --sky-glow: #a9d8f5;
    --deep: #0b63b8;
    --band-start: #0523c4;
    --band-end: #0b45e6;
    --title-shadow: #0a2fb8;
    --white: #ffffff;
  }
  html, body {
    margin: 0;
    padding: 0;
    width: 1200px;
    height: 675px;
    overflow: hidden;
    background: var(--white);
  }
  .series-card {
    position: relative;
    width: 1200px;
    height: 675px;
    overflow: hidden;
    background: var(--sky);
    font-family: "Cinzel", Georgia, serif;
  }
  .backdrop {
    position: absolute;
    inset: 0;
    background:
      radial-gradient(circle at 50% 33%, rgba(11, 99, 184, 0.55) 0, rgba(11, 99, 184, 0.35) 190px, rgba(43, 153, 227, 0) 210px),
      radial-gradient(ellipse 260px 140px at 50% 88%, rgba(169, 216, 245, 0.75), rgba(169, 216, 245, 0) 100%),
      linear-gradient(180deg, var(--sky) 0%, #3aa0e4 60%, var(--sky-light) 100%);
  }
  .series-title {
    position: absolute;
    left: 0;
    right: 0;
    top: 92px;
    margin: 0;
    text-align: center;
    color: var(--white);
    font-weight: 500;
    font-size: 108px;
    line-height: 115px;
    letter-spacing: -2px;
    text-transform: uppercase;
    text-shadow: 5px 5px 4px var(--title-shadow), 0 0 14px rgba(10, 47, 184, 0.35);
  }
  .series-title span { display: block; }
  .tagline-band {
    position: absolute;
    left: 0;
    top: 579px;
    width: 1200px;
    height: 60px;
    display: flex;
    align-items: center;
    justify-content: center;
    background: linear-gradient(90deg, var(--band-start), var(--band-end));
  }
  .tagline {
    margin: 0;
    color: var(--white);
    font-size: 31px;
    font-weight: 500;
    letter-spacing: 3px;
    text-transform: uppercase;
    white-space: nowrap;
  }
  .footer-strip {
    position: absolute;
    left: 0;
    top: 639px;
    width: 1200px;
    height: 36px;
    background: linear-gradient(90deg, rgba(11, 99, 184, 0.6), rgba(107, 184, 234, 0.3), rgba(11, 99, 184, 0.4));
  }
</style>
</head>
<body>
  <main class="series-card">
    <div class="backdrop" role="img" aria-label="Photo of open hands raised toward a glowing globe of the earth against a blue starry sky"></div>
    <h1 class="series-title">
      <span>Every</span>
      <span>Lantern</span>
      <span>Still</span>
      <span>Burning</span>
    </h1>
    <div class="tagline-band">
      <p class="tagline">Lorem Ipsum Lorem Ipsum Lorem Ipsum Lorem Ipsum</p>
    </div>
    <div class="footer-strip"></div>
  </main>
</body>
</html>
```